Electrical panel service sticker w Bucket truck & Logo

We have a rather plain sticker we put on lighting panels to remind customers who to call for service. We want to redesign them with brushed aluminum background. We want a remake of the sticker with the outline of a bucket truck. You'll need to find or draw the outling of a bucket truck maybe with the boom up slightly as we will get these stickers die cut.

We want LOGO with Ph.# and Email.
Electrical * Lighting * Sign Service

Target Market(s)

Commercial property managers

Industry/Entity Type

Property Management

Requirements
Must have
• Bucket Truck Outline

```html
<!DOCTYPE html>
<html lang="en">
<head>
<meta charset="utf-8">
<title>Brightline Fixture Services – Panel Service Sticker</title>
<link href="https://fonts.googleapis.com/css2?family=Saira:wght@500;600;700&display=swap" rel="stylesheet">
<style>
  :root {
    --page-bg: #e6e6e6;
    --sticker-white: #ffffff;
    --brand-red: #a11d21;
    --brand-navy: #263686;
    --ink: #1b1f3a;
    --ink-dark: #222222;
    --text-light: #ffffff;
  }
  * { box-sizing: border-box; margin: 0; padding: 0; }
  html, body {
    width: 1200px; height: 1200px; overflow: hidden;
    background: var(--page-bg);
    font-family: "Saira", Arial, sans-serif;
  }
  .sticker {
    position: absolute; left: 128px; top: 267px;
    width: 923px; height: 666px;
    box-shadow: 0 4px 14px rgba(0,0,0,0.18);
  }
  .info-panel {
    position: absolute; left: 0; top: 0; width: 509px; height: 550px;
    background: var(--sticker-white);
  }
  .service-panel {
    position: absolute; left: 509px; top: 0; width: 414px; height: 550px;
    background: var(--brand-red);
  }
  .contact-band {
    position: absolute; left: 0; top: 550px; width: 923px; height: 116px;
    background: var(--brand-navy);
    display: flex; align-items: center; justify-content: center;
  }
  .brand-name {
    position: absolute; left: 14px; top: 88px; width: 480px;
    display: flex; align-items: center; gap: 14px;
    color: var(--brand-red); font-weight: 700;
    font-size: 50px; line-height: 0.98; text-transform: uppercase;
    letter-spacing: 0.5px;
  }
  .brand-mark {
    flex: none; width: 34px; height: 34px; border-radius: 50%;
    background: var(--brand-red);
  }
  .tagline {
    position: absolute; left: 12px; top: 292px;
    font-weight: 600; font-size: 27px; color: var(--ink-dark);
    letter-spacing: 0.3px; white-space: nowrap;
  }
  .phone-icon { position: absolute; left: 13px; top: 420px; width: 72px; height: 72px; }
  .phone-label {
    position: absolute; left: 103px; top: 410px;
    font-weight: 600; font-size: 26px; color: var(--ink);
  }
  .phone-number {
    position: absolute; left: 101px; top: 438px;
    font-weight: 600; font-size: 54px; color: var(--ink);
    letter-spacing: 2px; white-space: nowrap;
  }
  .truck-illustration {
    position: absolute; left: 20px; top: 65px; width: 290px; height: 190px;
    background: rgba(255,255,255,0.18); border-radius: 6px;
  }
  .service-list {
    position: absolute; left: 18px; top: 305px; list-style: none;
  }
  .service-list li {
    display: flex; align-items: center; gap: 14px;
    color: var(--text-light); font-weight: 600; font-size: 50px;
    line-height: 68px; white-space: nowrap; letter-spacing: 0.5px;
  }
  .service-list li::before {
    content: ""; width: 15px; height: 15px; border-radius: 50%;
    background: var(--text-light); flex: none;
  }
  .email {
    color: var(--text-light); font-weight: 600; font-size: 50px;
    letter-spacing: 0.5px;
  }
</style>
</head>
<body>
  <main class="sticker">
    <section class="info-panel">
      <div class="brand-name"><span class="brand-mark"></span><span>Brightline<br>Fixture<br>Services</span></div>
      <p class="tagline">Trusted &amp; Reliable Lighting Experts</p>
      <svg class="phone-icon" viewBox="0 0 72 72" aria-hidden="true">
        <circle cx="36" cy="36" r="32" fill="none" stroke="#000" stroke-width="4"/>
        <path d="M30 18 l8 -3 l5 12 l-6 3 q-2 8 2 16 l6 -2 l4 12 l-8 3 q-14 -18 -11 -41z" fill="#000"/>
      </svg>
      <p class="phone-label">For Service Call</p>
      <p class="phone-number">877-555-0148</p>
    </section>
    <section class="service-panel">
      <div class="truck-illustration" role="img" aria-label="White outline of a bucket truck with its boom raised"></div>
      <ul class="service-list">
        <li>ELECTRICAL</li>
        <li>LIGHTING</li>
        <li>SIGN SERVICE</li>
      </ul>
    </section>
    <footer class="contact-band">
      <p class="email">Service@BrightlineFixture.com</p>
    </footer>
  </main>
</body>
</html>
```